Promotional business a5 Notepad design

I am looking for a custom a5 notepad design as a promotional item to give away to customers etc.
Attached will be a desk planner we had designed feel free to use as a reference.
We want the notepad to have lines running horizontal not squares like the desk planner example.

Industry/Entity Type

Hydraulic / industrial

Colors

Designer to choose colors to be used in the design.

```html
<!DOCTYPE html>
<html lang="en">
<head>
<meta charset="utf-8">
<title>Meridian Hose – A5 Notepad</title>
<link href="https://fonts.googleapis.com/css2?family=Arimo:wght@400;700&display=swap" rel="stylesheet">
<style>
  :root {
    --backdrop: #a1a1a3;
    --paper: #ffffff;
    --brand-blue: #1530bd;
    --steel: #a7a7a7;
    --steel-light: #d6d6d6;
    --rule: #6f6f6f;
    --mark: #1d1d1d;
    --on-blue: #ffffff;
  }
  * { margin: 0; padding: 0; box-sizing: border-box; }
  html, body { width: 1200px; height: 900px; overflow: hidden; }
  body { background: var(--backdrop); font-family: "Arimo", Arial, sans-serif; position: relative; }

  .notepad {
    position: absolute; left: 325px; top: 60px;
    width: 550px; height: 780px;
    background: var(--paper);
  }

  .header-band {
    position: absolute; left: 1px; top: 33px; width: 549px; height: 18px;
    background: var(--brand-blue);
  }
  .header-steel {
    position: absolute; left: 1px; top: 53px; width: 549px; height: 9px;
    background: linear-gradient(90deg, var(--steel) 0%, var(--steel) 45%, var(--steel-light) 80%, var(--steel) 100%);
  }
  .header-gap {
    position: absolute; left: 249px; top: 30px; width: 4px; height: 34px;
    background: var(--paper);
  }
  .brand-dot {
    position: absolute; left: 36px; top: 26px; width: 50px; height: 50px;
    border-radius: 50%; background: var(--mark); border: 3px solid var(--paper);
  }
  .brand-name {
    position: absolute; left: 94px; top: 33px; height: 18px;
    line-height: 18px; font-size: 17px; font-weight: 700; letter-spacing: 1px;
    color: var(--on-blue);
  }

  .ruled-lines {
    position: absolute; left: 37px; top: 123px; width: 475px;
  }
  .ruled-lines li {
    list-style: none; height: 29.5px;
    border-top: 1px solid var(--rule);
  }
  .ruled-lines li:last-child { height: 0; }

  .footer {
    position: absolute; left: 0; bottom: 0; width: 550px; height: 56px;
    background: var(--brand-blue); color: var(--on-blue);
    text-align: center;
  }
  .footer .area { font-size: 11px; margin-top: 11px; display: flex; justify-content: center; align-items: center; gap: 4px; }
  .footer .contacts { font-size: 12.5px; margin-top: 5px; display: flex; justify-content: center; align-items: center; gap: 5px; }
  .footer .contacts .item { display: inline-flex; align-items: center; gap: 5px; margin-right: 4px; }
  .footer svg { fill: var(--on-blue); }
</style>
</head>
<body>
  <main class="notepad">
    <div class="header-band"></div>
    <div class="header-steel"></div>
    <div class="header-gap"></div>
    <div class="brand-dot"></div>
    <div class="brand-name">MERIDIAN HOSE</div>

    <ul class="ruled-lines">
      <li></li><li></li><li></li><li></li><li></li>
      <li></li><li></li><li></li><li></li><li></li>
      <li></li><li></li><li></li><li></li><li></li>
      <li></li><li></li><li></li><li></li><li></li>
    </ul>

    <footer class="footer">
      <p class="area">
        <svg width="8" height="11" viewBox="0 0 8 11"><path d="M4 0a4 4 0 0 1 4 4c0 3-4 7-4 7S0 7 0 4a4 4 0 0 1 4-4zm0 2.3a1.7 1.7 0 1 0 0 3.4 1.7 1.7 0 0 0 0-3.4z"/></svg>
        Servicing The Northvale Metropolitan Area
      </p>
      <p class="contacts">
        <span class="item">
          <svg width="9" height="9" viewBox="0 0 10 10"><path d="M2 0l2 2.5-1.2 1.3a6 6 0 0 0 3.4 3.4L7.5 6 10 8l-1.5 2C4 10 0 6 0 1.5z"/></svg>
          08 5550 1234
        </span>
        <span class="item">
          <svg width="9" height="9" viewBox="0 0 10 10"><path d="M2 0l2 2.5-1.2 1.3a6 6 0 0 0 3.4 3.4L7.5 6 10 8l-1.5 2C4 10 0 6 0 1.5z"/></svg>
          0400 555 219
        </span>
        <span class="item">
          <svg width="10" height="7" viewBox="0 0 10 7"><path d="M0 0h10v7H0zM0.8 0.8L5 4 9.2 0.8" stroke="#1530bd" stroke-width="0.8"/></svg>
          hello@meridianhose.com.au
        </span>
      </p>
    </footer>
  </main>
</body>
</html>
```